Economics and Investing for women with a humorous narrative

I need a logo and business card design for my company:
The Velvet Almanac LLC. TVA is an educational website dedicated to translating the language of economics and investing into concepts that are interesting, easy to understand and funny.
As the target market is for women, the card needs to be NON traditional in terms of finance and investing. No pictures of charts, currencies, stock markets etc. This needs to be colorful , inviting and memorable.
The driver of the site is to present difficult concepts with a humorous tilt. If Gregory Tandy (A Paper Orchard) collaborated with Lila Brandt what would it look like?

Reason: I don't think I did a good enough job of explaining what I was looking for including the type of color palette. I asked that the cards NOT look so corporate. I have updated my brief and included 3 pictures of a color scheme I like along with design. I also update the information to be included on the card.

Target Market(s)

Women 30-50

Industry/Entity Type

Business

Contact Information for Business Card

The Velvet Almanac LLC
Dana Holloway , CEO
482 Wexley Street
Suite 2300
New York, New York 10017

Phone: 212-555-0143
TheVelvetAlmanac.com
Email: dana@thevelvetalmanac.com

Font styles to use
Other font styles liked:
• LustPro Demi No.3

Requirements
Must have
• Gravitas, bold warm colors, the antithesis of modest
Nice to have
• Isn't this why I am hiring designers?
Should not have
• Charts, graphs, numbers, currency, stock or bond market pictures, any reference to investing . Do not want this to look like a boring investment business card

```html
<!DOCTYPE html>
<html lang="en">
<head>
<meta charset="utf-8">
<title>The Velvet Almanac LLC — Business Card</title>
<link rel="stylesheet" href="https://fonts.googleapis.com/css2?family=Open+Sans:wght@400;600;700&display=swap">
<style>
  :root {
    --berry: #7a1f4b;
    --berry-deep: #6a1740;
    --coral: #e4603c;
    --gold: #f2b134;
    --ink: #3a2a2e;
    --paper: #fffaf3;
    --cream: #fff4e2;
    --backdrop: #efe6dc;
  }
  * { box-sizing: border-box; margin: 0; padding: 0; }
  html, body {
    width: 1200px; height: 844px; overflow: hidden;
    background: var(--backdrop);
    font-family: "Open Sans", Arial, sans-serif;
  }
  .stage {
    position: relative; width: 1200px; height: 844px;
    display: flex; align-items: center; justify-content: center; gap: 60px;
  }
  .card {
    position: relative; width: 520px; height: 298px; overflow: hidden;
    box-shadow: 0 6px 18px rgba(80,30,20,0.18);
  }
  .card--front { background: var(--paper); border-top: 6px solid var(--coral); }
  .card--back { background: var(--berry-deep); border-bottom: 6px solid var(--gold); }

  .brand {
    position: absolute; top: 34px; right: 34px;
    display: flex; align-items: center; gap: 9px;
  }
  .brand__dot {
    width: 14px; height: 14px; border-radius: 50%; background: var(--coral);
  }
  .brand__name {
    color: var(--berry); font-weight: 700; font-size: 15px; letter-spacing: 0.2px;
    text-transform: uppercase;
  }

  .contact {
    position: absolute; left: 34px; top: 116px; color: var(--ink);
  }
  .contact__name {
    color: var(--berry); font-weight: 700; font-size: 19px; margin-bottom: 10px;
  }
  .contact__title { font-size: 12px; font-weight: 600; color: var(--coral); vertical-align: 4px; }
  .contact__address { font-size: 13.5px; line-height: 1.3; margin-bottom: 12px; }
  .contact__list { list-style: none; font-size: 13.5px; line-height: 1.3; }
  .contact__list li { display: flex; align-items: center; gap: 8px; margin-bottom: 2px; }
  .contact__list svg { width: 11px; height: 11px; flex: none; }

  .back__name {
    position: absolute; right: 30px; bottom: 72px;
    color: var(--cream); font-weight: 700; font-size: 21px; text-transform: uppercase;
    letter-spacing: 0.2px;
  }
  .back__name small { font-size: 10px; color: var(--gold); vertical-align: 8px; }
</style>
</head>
<body>
<main class="stage">
  <section class="card card--front" aria-label="Business card front">
    <div class="brand">
      <span class="brand__dot"></span>
      <span class="brand__name">The Velvet Almanac LLC</span>
    </div>
    <div class="contact">
      <p class="contact__name">Dana Holloway <span class="contact__title">, CEO</span></p>
      <p class="contact__address">482 Wexley Street Suite 2300<br>New York, New York 10017</p>
      <ul class="contact__list">
        <li>
          <svg viewBox="0 0 12 12" aria-hidden="true"><path fill="var(--coral)" d="M2.5 0.8l1.8 2.3-1 1.2c.7 1.5 1.9 2.7 3.4 3.4l1.2-1 2.3 1.8-.9 1.9C5.4 10.2 1.8 6.6 1 2z"/></svg>
          212-555-0143
        </li>
        <li>
          <svg viewBox="0 0 12 12" aria-hidden="true"><rect x="0.5" y="2" width="11" height="8" fill="var(--coral)"/><path d="M0.8 2.4L6 6.6l5.2-4.2" stroke="#fff" stroke-width="1" fill="none"/></svg>
          dana@thevelvetalmanac.com
        </li>
        <li>
          <svg viewBox="0 0 12 12" aria-hidden="true"><circle cx="6" cy="6" r="5" fill="none" stroke="var(--coral)" stroke-width="1"/><path d="M1 6h10M6 1c-2.5 3-2.5 7 0 10M6 1c2.5 3 2.5 7 0 10" stroke="var(--coral)" stroke-width="0.8" fill="none"/></svg>
          www.TheVelvetAlmanac.com
        </li>
      </ul>
    </div>
  </section>

  <section class="card card--back" aria-label="Business card back">
    <p class="back__name">The Velvet Almanac <small>LLC</small></p>
  </section>
</main>
</body>
</html>
```